Letterhead Design Project

I need a simple, clean and corporate letterhead & follow-on letterhead.
The follow-on letterhead should just have the logo only.
Final File Specs:
Full Bleed Size (starting document size)
213 x 300 mm
2517 x 3544 pixels
* Finished artwork should use the full bleed dimensions for best results.
Document Trim Size (final size after being cut)
210 x 297 mm
2480 x 3508 pixels
* Please be sure to keep all text within the safe margin.
Resolution 300 DPI
Accepted file types:-
Adobe Acrobat 9 Document (*.pdf) (recommended)
Adobe Illustrator CS3 Artwork (*.ai) (recommended)
Adobe Photoshop CS3 Image (*.psd) (recommended)
Bitmap Image (*.bmp)
GIF Image (*.gif)
JPEG Image (*.jpg,*.jpeg)
Microsoft PowerPoint 2010 Document (*.ppt)
Microsoft Publisher 2010 Document (*.pub)
Microsoft Word 2010 Document (*.doc)
PCX Image (*.pcx)
PICT Image (*.pic,*.pict,*.pct)
PNG Image (*.png)
PostScript Document (*.ps)
TIF Image (*.tif,*.tiff)
Windows Enhanced Metafile (*.emf)
Windows Metafile (*.wmf)
Requirements
Must have
- My letterhead must have:-
- Logo
- ACN - 418 572 906
- address - Suite 8, 19 Heron St, Maroubra, NSW 2035
- phone - (02) 9361 4258
- fax - (02) 9517 3046
- email - info@brimtarsafety.com.au
- web - www.brimtarsafety.com.au
Follow-on letterhead should have the logo only

```html
<!DOCTYPE html>
<html lang="en">
<head>
<meta charset="utf-8">
<title>Brimtar Letterhead</title>
<link rel="stylesheet" href="https://fonts.googleapis.com/css2?family=Montserrat:wght@500;600&display=swap">
<style>
  :root {
    --ink: #1b1f5c;
    --rule: #1a1a1a;
    --paper: #ffffff;
  }
  html, body {
    margin: 0;
    padding: 0;
    width: 840px;
    height: 1200px;
    overflow: hidden;
    background: var(--paper);
  }
  .letterhead {
    position: relative;
    width: 840px;
    height: 1200px;
    background: var(--paper);
    font-family: "Montserrat", Arial, sans-serif;
    color: var(--ink);
  }
  .brand {
    position: absolute;
    left: 18px;
    top: 58px;
    width: 190px;
    display: flex;
    align-items: center;
    gap: 10px;
  }
  .brand-mark {
    flex: none;
    width: 50px;
    height: 50px;
    background: var(--ink);
    border-radius: 7px;
  }
  .brand-name {
    font-weight: 600;
    font-size: 29px;
    letter-spacing: -0.3px;
    line-height: 1;
    color: var(--ink);
    white-space: nowrap;
  }
  .contact {
    position: absolute;
    left: 220px;
    top: 18px;
    margin: 0;
    padding: 0;
    list-style: none;
    font-weight: 600;
    font-size: 18px;
    line-height: 20.4px;
    white-space: nowrap;
  }
  .header-rule {
    position: absolute;
    left: 0;
    top: 149px;
    width: 840px;
    height: 0;
    border-top: 1.5px solid var(--rule);
  }
</style>
</head>
<body>
  <div class="letterhead">
    <header>
      <div class="brand">
        <div class="brand-mark"></div>
        <span class="brand-name">Brimtar</span>
      </div>
      <ul class="contact">
        <li>ACN - 418 572 906</li>
        <li>Address - Suite 8, 19 Heron St, Maroubra, NSW 2035</li>
        <li>Phone - (02) 9361 4258</li>
        <li>Fax - (02) 9517 3046</li>
        <li>Email - info@brimtarsafety.com.au</li>
        <li>Web - www.brimtarsafety.com.au</li>
      </ul>
      <div class="header-rule"></div>
    </header>
  </div>
</body>
</html>
```